High-end Oceanfront Real Estate Group Needs Clean, Modern Web Design

I’m looking for a clean, professional, modern and beautiful homepage web design for a Real Estate group in Southern California, USA.

The group/company is “Marlow on the Tide,” and they specialize in high end (i.e. expensive), oceanfront real estate in the Orange County area.

The look and feel of the page should accentuate the brand qualities: luxurious/expensive, professional, and beautiful (Orange County is one of the most beautiful areas in all the US and we would love the site to emphasize the beautiful beaches and scenery it has to offer).

Looks we like:
• www.brantleyhomesrealty.example
• www.keptbyvane.example -- I think the design is pretty out-dated in this site, but I like the organization/layout of the site

Header Tags (I don’t know if we can fit all of these, may need a side-menu, but I’d prefer header title only if possible):
• Welcome
• Featured Listings
• Previously Sold
• Sell
• Property Search
• Team
• Videos
• Blog
• Explore O.C.
• Contact

I have attached the beach and logo pics that we would like to use as the header, a few pictures of the team, and one sample home/view pic which can be used in any of the other sections (for pictures of the homes, just find expensive oceanfront houses and that will be fine).

I promise to provide feedback to each and every design submission. I appreciate the hard work that all of you are putting into your designs. There can be only one contest winner, but I hope to give all of you helpful feedback to submit the best designs possible!

Target Market(s)

Very wealthy home owners of oceanfront properties. These properties are worth several millions of dollars, and thus the site and brand needs to be targeted to very wealthy, successful individuals and families (both US and international buyers).

Industry/Entity Type

Real Estate

Number of Pages Required

2 page

Requirements
Must have
• I don’t want to give too many requirements, because I want to let you all be creative. However, here are the few Must Haves:
• Must submit 2 page designs (a home page and a sub page)
• Must use logo provided
• Focus is mostly on homes, but I would like to include some beach/ocean imagery as well
• The first “item” on the home page should be an accordion/slider which shows pictures of homes and with 1 line of text: “List with the Leader” and two link buttons: “Sell Your Home” and “Buy Your Home”
• Color palette needs to be mainly blues--to match ocean and sky blue
• Exported in all major formats (psd,ai,eps,png,jpeg,etc)
Nice to have
• We don’t necessarily need all of these, but would like to feature most:
• List of videos
• “Meet the Team”—brief team bios and pics
• Link(s) to Blog
• “List with the Leader” – section on why they should choose this firm
• Featured Listings
• Previously Sold

```html
<!DOCTYPE html>
<html lang="en">
<head>
<meta charset="utf-8">
<title>Marlow on the Tide — Oceanfront Real Estate</title>
<link href="https://fonts.googleapis.com/css2?family=Open+Sans:wght@400;600;700;800&family=Oswald:wght@400;500&display=swap" rel="stylesheet">
<style>
:root{
  --blue:#2f7fd0;
  --blue-dark:#1d5fa8;
  --blue-deep:#0f2f5c;
  --sky:#8fc4ee;
  --ink:#2b2b2b;
  --muted:#6f6f6f;
  --line:#d9dde2;
  --grey-bg:#ececec;
  --black:#121212;
  --white:#ffffff;
}
*{box-sizing:border-box;margin:0;padding:0}
html,body{width:1200px;height:3822px;overflow:hidden}
body{font-family:"Open Sans",Arial,sans-serif;color:var(--ink);background:var(--white);position:relative}
section,header,footer{position:absolute;left:0;width:1200px}
.abs{position:absolute}
.photo{position:absolute}

/* header */
.site-header{top:0;height:115px;background:linear-gradient(180deg,#3b8fe0,#1f6cc2);z-index:2}
.brand{left:130px;top:18px;display:flex;align-items:center;gap:12px}
.brand-mark{width:26px;height:26px;background:var(--sky)}
.brand-name{color:var(--white);font-weight:600;font-size:22px;letter-spacing:.5px}
.socials{right:230px;top:12px;display:flex;gap:10px}
.socials span{width:30px;height:30px;border-radius:50%;border:2px solid var(--white)}
.lang{right:140px;top:14px;width:62px;height:24px;border-radius:12px;border:1.5px solid var(--white);color:var(--white);font-size:11px;display:flex;align-items:center;justify-content:center}
.main-nav{left:340px;top:66px;display:flex;gap:4px}
.main-nav a{color:var(--white);text-decoration:none;font-size:13px;padding:7px 14px}
.main-nav a.active{background:#c9d3dd;color:#333}

/* hero */
.hero{top:115px;height:485px;overflow:hidden}
.hero .photo{inset:0;background:linear-gradient(180deg,#123a78 0%,#1e4e8e 35%,#3c4f6a 60%,#6b5a44 80%,#1b2a3e 100%)}
.hero-title{left:0;width:1200px;top:188px;text-align:center;font-family:"Oswald",sans-serif;font-size:44px;color:var(--white);letter-spacing:.5px}
.hero-actions{left:0;width:1200px;top:250px;display:flex;justify-content:center;gap:22px}
.hero-btn{height:58px;padding:0 24px;background:rgba(20,20,25,.55);color:var(--white);font-family:"Oswald",sans-serif;font-size:27px;display:flex;align-items:center;gap:14px}
.hero-btn .ring{width:28px;height:28px;border:2px solid var(--white);border-radius:50%;display:flex;align-items:center;justify-content:center}
.hero-arrow{top:212px;width:38px;height:38px;border-radius:50%;background:var(--white);display:flex;align-items:center;justify-content:center}
.thumb-strip{left:0;top:368px;width:1200px;height:117px;background:rgba(10,20,35,.55)}
.thumbs{left:143px;top:12px;display:flex;gap:30px}
.thumbs span{width:155px;height:92px;border:3px solid var(--white)}
.strip-arrow{top:44px;color:var(--white);font-size:26px}

/* search */
.search{top:600px;height:165px;background:#f4f5f6;border-bottom:1px solid var(--line)}
.search h2{position:absolute;left:133px;top:22px;font-size:21px;font-weight:700;color:#1c3f6e}
.field{position:absolute;height:34px;background:var(--white);border:1px solid #c8ccd1;font-size:12px;color:#555;display:flex;align-items:center;justify-content:space-between;padding:0 10px}
.field.select::after{content:"";width:7px;height:7px;border-right:2px solid #555;border-bottom:2px solid #555;transform:rotate(45deg) translateY(-3px)}
.to-label{position:absolute;left:372px;top:128px;font-size:12px}
.search-btn{position:absolute;left:940px;top:120px;width:125px;height:34px;background:var(--black);color:var(--white);font-size:12px;display:flex;align-items:center;justify-content:center}

/* welcome */
.welcome{top:765px;height:267px;text-align:center}
.welcome h1{margin-top:55px;font-size:34px;font-weight:400;color:#333}
.welcome .sub{font-size:12px;letter-spacing:5px;color:#777;margin-top:14px;border-top:1px solid var(--line);display:inline-block;padding:6px 40px 0}
.welcome p{width:960px;margin:14px auto 0;font-size:13px;line-height:20px;color:#444}

/* featured */
.featured{top:1032px;height:382px;background:var(--grey-bg)}
.section-title{position:absolute;left:0;width:1200px;text-align:center;font-size:24px;color:#333}
.listing{position:absolute;top:86px;width:207px;height:268px;background:var(--white)}
.listing .photo{left:0;top:0;width:207px;height:144px}
.price{position:absolute;left:0;top:112px;background:var(--blue);color:var(--white);font-size:12px;font-weight:700;padding:5px 14px}
.listing h3{position:absolute;left:8px;top:152px;font-size:16px;font-weight:700}
.listing .loc{position:absolute;left:8px;top:175px;font-size:12px;color:#666}
.btn-blue{position:absolute;background:var(--blue);color:var(--white);font-size:13px;font-weight:700;display:flex;align-items:center;justify-content:center}
.listing .btn-blue{left:0;top:226px;width:207px;height:36px}

/* explore */
.explore{top:1414px;height:426px;overflow:hidden}
.explore .photo{inset:0;background:linear-gradient(180deg,#24365a,#182a48 60%,#0f1d33)}
.explore h2{position:absolute;left:0;width:1200px;top:34px;text-align:center;color:var(--white);font-size:30px;font-weight:700}
.explore p{position:absolute;left:150px;width:900px;top:90px;text-align:center;color:#e6ebf2;font-size:13px;line-height:19px}
.explore-btn{position:absolute;left:540px;top:183px;width:140px;height:40px;border-radius:20px;border:2px solid var(--white);background:var(--blue-dark);color:var(--white);font-size:13px;display:flex;align-items:center;justify-content:center}
.attraction{position:absolute;top:270px;width:112px;text-align:center}
.attraction .icon{width:112px;height:80px;border:3px solid var(--white);background:#e9f1fb;position:relative}
.attraction .icon i{position:absolute;inset:12px 22px;background:var(--blue-dark);display:block}
.attraction span{display:block;color:var(--white);font-size:11px;font-weight:700;margin-top:8px;line-height:14px}

/* sold */
.sold{top:1840px;height:340px}
.sold-frame{position:absolute;left:130px;top:55px;width:942px;height:272px;border:2px solid #e2e5e9;background:#fafafa}
.sold-tab{position:absolute;left:480px;top:38px;width:240px;height:40px;background:var(--blue);color:var(--white);font-size:15px;font-weight:700;display:flex;align-items:center;justify-content:center}
.sold-card{position:absolute;top:90px;width:206px}
.sold-card .photo{position:relative;height:150px}
.sold-card .plus{position:absolute;left:94px;top:120px;color:var(--white);font-size:22px}
.sold-meta{display:flex;justify-content:space-between;font-size:11px;font-weight:700;padding:7px 4px}
.sold-meta b{color:var(--blue)}
.sold-card .btn-blue{position:relative;height:28px;font-size:11px}

/* team */
.team{top:2180px;height:483px}
.team h2{position:absolute;left:0;width:1200px;text-align:center;top:12px;font-size:22px;font-weight:700}
.team .rule{position:absolute;left:540px;top:50px;width:120px;border-top:1px solid var(--line)}
.bubble{position:absolute;border:1.5px solid #cfd4da;border-radius:12px;background:var(--white);padding:22px 26px;font-size:12px;line-height:18px;color:#555}
.avatar{position:absolute;width:86px;height:86px;border-radius:50%;background:linear-gradient(160deg,#c9b7a3,#7d6a58);border:4px solid #e6e8eb}
.member{position:absolute;font-size:17px;font-weight:800;color:#333}
.member small{display:block;font-size:12px;font-style:italic;font-weight:400;color:#666}

/* consult */
.consult{top:2663px;height:305px;overflow:hidden}
.consult .photo{inset:0;background:linear-gradient(90deg,#bcd6ee,#e4eef8 60%,#cfe0f0)}
.consult-panel{position:absolute;left:0;top:0}
.consult h2{position:absolute;left:200px;width:300px;top:80px;text-align:right;color:var(--white);font-size:20px;font-weight:400}
.consult h2 b{font-weight:700}
.consult p{position:absolute;left:160px;width:340px;top:115px;text-align:right;color:var(--white);font-size:12px;line-height:20px}
.mail-ring{position:absolute;left:508px;top:96px;width:112px;height:112px;border-radius:50%;background:#d9dde2;display:flex;align-items:center;justify-content:center}
.input{position:absolute;left:680px;width:305px;height:38px;border:1px solid rgba(255,255,255,.9);background:rgba(255,255,255,.3);color:var(--white);font-size:13px;padding:8px 10px}
.consult .btn-blue{left:680px;top:252px;width:80px;height:34px}

/* blog */
.blog{top:2968px;height:522px}
.blog h2{position:absolute;left:0;width:1200px;text-align:center;top:36px;font-size:22px;font-weight:700}
.post{position:absolute;top:127px;width:285px}
.post .photo{left:0;top:0;width:285px;height:190px}
.date{position:absolute;left:0;top:0;width:36px;background:var(--blue);color:var(--white);text-align:center;font-size:11px;font-weight:700;padding:6px 0;line-height:16px}
.date b{display:block;font-size:15px}
.date-icon{position:absolute;left:0;width:36px;height:36px;background:#222;display:flex;align-items:center;justify-content:center}
.post h3{position:absolute;left:60px;top:204px;font-size:14px;font-weight:700}
.post .meta{position:absolute;left:60px;top:226px;font-size:9px;color:#888}
.post p{position:absolute;left:60px;top:242px;width:220px;font-size:11px;line-height:15px;color:#555}
.post .btn-blue{left:60px;top:300px;width:86px;height:28px;border-radius:14px;font-size:11px}

/* footer */
.site-footer{top:3503px;height:319px;background:var(--black);color:var(--white)}
.site-footer h4{position:absolute;font-size:15px;font-weight:700}
.links{position:absolute;top:74px;font-size:12px;line-height:27px;list-style:none}
.links li::before{content:"› ";color:#aaa}
.follow{position:absolute;left:133px;top:200px;display:flex;align-items:center;gap:10px;font-size:14px;font-weight:700}
.follow span{width:26px;height:26px;border-radius:50%;background:#3a3a3a}
.video-tab{position:absolute;left:445px;top:-14px;width:315px;height:240px;background:#1c1c1c}
.video{position:absolute;left:20px;top:76px;width:275px;height:140px;background:linear-gradient(160deg,#cfd9e2,#6f8aa3 60%,#3c4c5c);border:3px solid var(--white)}
.video-bar{position:absolute;left:0;right:0;bottom:0;height:22px;background:rgba(0,0,0,.55)}
.play{position:absolute;left:112px;top:44px;width:46px;height:34px;background:rgba(0,0,0,.8);border-radius:6px;display:flex;align-items:center;justify-content:center}
.news-box{position:absolute;left:810px;top:74px;width:262px;height:126px;background:#2a2a2a;padding:12px 14px;font-size:12px;line-height:17px}
.news-input{position:absolute;left:14px;top:84px;width:196px;height:30px;background:var(--white);color:#777;font-size:11px;font-style:italic;padding:7px 10px}
.news-go{position:absolute;left:214px;top:84px;width:34px;height:30px;background:var(--blue);font-size:12px;font-weight:700;display:flex;align-items:center;justify-content:center}
.copyright{position:absolute;left:0;top:281px;width:1200px;height:38px;border-top:1px solid #2d2d2d;text-align:center;font-size:11px;color:#bbb;padding-top:12px}
</style>
</head>
<body>

<header class="site-header">
  <div class="abs brand"><span class="brand-mark"></span><span class="brand-name">Marlow on the Tide</span></div>
  <div class="abs socials" aria-label="Social links"><span></span><span></span><span></span><span></span></div>
  <div class="abs lang">English ▾</div>
  <nav class="abs main-nav">
    <a class="active" href="#">Home</a><a href="#">About us</a><a href="#">Property Search</a><a href="#">Team</a><a href="#">Videos</a><a href="#">Blog</a><a href="#">Explore O.C</a><a href="#">Contact</a>
  </nav>
</header>

<section class="hero">
  <div class="photo" role="img" aria-label="Oceanfront luxury villa with pool at dusk"></div>
  <h1 class="abs hero-title">LOOKING FOR A LUXURIOUS &amp; BEAUTIFUL HOME</h1>
  <div class="abs hero-actions">
    <div class="hero-btn">SELL YOUR HOME <span class="ring"><svg width="10" height="12" viewBox="0 0 10 12"><path d="M2 1l6 5-6 5" fill="none" stroke="#fff" stroke-width="2"/></svg></span></div>
    <div class="hero-btn">BUY YOUR HOME <span class="ring"><svg width="10" height="12" viewBox="0 0 10 12"><path d="M2 1l6 5-6 5" fill="none" stroke="#fff" stroke-width="2"/></svg></span></div>
  </div>
  <div class="abs hero-arrow" style="left:65px"><svg width="12" height="14" viewBox="0 0 12 14"><path d="M9 1L3 7l6 6" fill="none" stroke="#222" stroke-width="3"/></svg></div>
  <div class="abs hero-arrow" style="right:65px"><svg width="12" height="14" viewBox="0 0 12 14"><path d="M3 1l6 6-6 6" fill="none" stroke="#222" stroke-width="3"/></svg></div>
  <div class="abs thumb-strip">
    <span class="abs strip-arrow" style="left:112px">‹</span>
    <div class="abs thumbs">
      <span class="photo" style="position:static;background:linear-gradient(160deg,#4a7fb8,#2a5a3c)" role="img" aria-label="Villa thumbnail"></span>
      <span style="background:linear-gradient(160deg,#6fa6d8,#3f6d4a)" role="img" aria-label="Palm garden thumbnail"></span>
      <span style="background:linear-gradient(160deg,#2a4e7e,#a07a52)" role="img" aria-label="Evening house thumbnail"></span>
      <span style="background:linear-gradient(160deg,#dfe6ee,#8aa1b8)" role="img" aria-label="Modern home thumbnail"></span>
      <span style="background:linear-gradient(160deg,#5b9ad6,#2f7a9a)" role="img" aria-label="Pool thumbnail"></span>
      <span style="background:linear-gradient(160deg,#7fb3e3,#40708f)" role="img" aria-label="Coastal view thumbnail"></span>
    </div>
    <span class="abs strip-arrow" style="right:112px">›</span>
  </div>
</section>

<section class="search">
  <h2>Search Commercial REAL ESTATE LISTINGS</h2>
  <div class="field select" style="left:133px;top:65px;width:322px">Property Type</div>
  <div class="field" style="left:555px;top:65px;width:370px">Type Location or Project or Keyword</div>
  <div class="field select" style="left:133px;top:120px;width:220px">Min Price</div>
  <span class="to-label">To</span>
  <div class="field select" style="left:405px;top:120px;width:235px">Max Price</div>
  <div class="field select" style="left:670px;top:120px;width:250px">Posted by: All</div>
  <div class="search-btn">Search <svg style="margin-left:6px" width="12" height="12" viewBox="0 0 12 12"><circle cx="5" cy="5" r="3.5" fill="none" stroke="#fff" stroke-width="1.5"/><path d="M8 8l3 3" stroke="#fff" stroke-width="1.5"/></svg></div>
</section>

<section class="welcome">
  <h1>WELCOME TO MARLOW</h1>
  <div class="sub">ON THE TIDE</div>
  <p>We represent the finest oceanfront homes along the Orange County coast, guiding buyers and sellers with care, discretion and deep local knowledge. From quiet cliffside retreats to grand estates on the sand, our team pairs every client with a home that fits the way they wish to live. Each sale is handled with patience, clear advice and close attention, so that moving to the shore feels calm and well planned from the first visit to the final signature.</p>
</section>

<section class="featured">
  <h2 class="section-title" style="top:28px">Featured Listings</h2>
  <div class="listing" style="left:133px">
    <div class="photo" role="img" aria-label="Palm-lined villa with pool" style="background:linear-gradient(160deg,#6aa9e0,#3f7d55 70%,#c9b18a)"></div>
    <div class="price">$ 1,499,000</div><h3>18400 Tideline View</h3><div class="loc">Pacific Coast</div>
    <div class="btn-blue">View More</div>
  </div>
  <div class="listing" style="left:375px">
    <div class="photo" role="img" aria-label="Stone house with pool" style="background:linear-gradient(160deg,#5c92cf,#8b7357 60%,#3b6b8e)"></div>
    <div class="price">$ 1,499,000</div><h3>Harbor Crest Home</h3><div class="loc">Pico Blvd</div>
    <div class="btn-blue">View More</div>
  </div>
  <div class="listing" style="left:618px">
    <div class="photo" role="img" aria-label="Modern villa at sunset" style="background:linear-gradient(160deg,#2c4f82,#b8864e 60%,#3a4f66)"></div>
    <div class="price">$ 1,499,000</div><h3>Seabright Estate</h3><div class="loc">Pico Blvd</div>
    <div class="btn-blue">View More</div>
  </div>
  <div class="listing" style="left:860px">
    <div class="photo" role="img" aria-label="Contemporary home at dusk" style="background:linear-gradient(160deg,#4b79b4,#9c6a44 60%,#2e3f55)"></div>
    <div class="price">$ 1,499,000</div><h3>Cliffside Retreat</h3><div class="loc">Pico Blvd</div>
    <div class="btn-blue">View More</div>
  </div>
</section>

<section class="explore">
  <div class="photo" role="img" aria-label="Coastal home lit at night"></div>
  <h2>EXPLORE ORANGE COUNTY</h2>
  <p>From sunlit beaches and quiet coves to lively harbors and family parks, Orange County offers a rich life by the water. Discover the places our clients love most, each just a short drive from home, and see why so many families choose to settle along this coast.</p>
  <div class="explore-btn">EXPLORE MORE</div>
  <div class="attraction" style="left:178px"><div class="icon" role="img" aria-label="Berry farm illustration"><i></i></div><span>Harbor Berry Farm</span></div>
  <div class="attraction" style="left:331px"><div class="icon" role="img" aria-label="Castle illustration"><i></i></div><span>Castleview Park</span></div>
  <div class="attraction" style="left:484px"><div class="icon" role="img" aria-label="Stadium illustration"><i></i></div><span>Anaheim Ballpark</span></div>
  <div class="attraction" style="left:632px"><div class="icon" role="img" aria-label="Beach park illustration"><i></i></div><span>Tidewater Cove Park</span></div>
  <div class="attraction" style="left:780px"><div class="icon" role="img" aria-label="Zoo illustration"><i></i></div><span>Coastal Wildlife Zoo</span></div>
  <div class="attraction" style="left:933px"><div class="icon" role="img" aria-label="Surfing illustration"><i></i></div><span>Coastline Surf Museum</span></div>
</section>

<section class="sold">
  <div class="sold-frame"></div>
  <div class="sold-tab">SOLD PROPERTIES</div>
  <div class="sold-card" style="left:153px"><div class="photo" role="img" aria-label="Living room with ocean view" style="background:linear-gradient(160deg,#9cc3e6,#3d6f9c)"></div><span class="plus">+</span><div class="sold-meta">10250 Harbor ct12 <b>$120548</b></div><div class="btn-blue">SOLD OUT</div></div>
  <div class="sold-card" style="left:383px"><div class="photo" role="img" aria-label="Villa with pool" style="background:linear-gradient(160deg,#5a9a4a,#49a3d8)"></div><span class="plus">+</span><div class="sold-meta">10250 Harbor ct12 <b>$120548</b></div><div class="btn-blue">SOLD OUT</div></div>
  <div class="sold-card" style="left:613px"><div class="photo" role="img" aria-label="Resort with palms" style="background:linear-gradient(160deg,#4f8fd0,#7b8a52 60%,#b7916a)"></div><span class="plus">+</span><div class="sold-meta">10250 Harbor ct12 <b>$120548</b></div><div class="btn-blue">SOLD OUT</div></div>
  <div class="sold-card" style="left:843px"><div class="photo" role="img" aria-label="Hillside home by the sea" style="background:linear-gradient(160deg,#6ea7dc,#2f6aa0 60%,#8f7a62)"></div><span class="plus">+</span><div class="sold-meta">10250 Harbor ct12 <b>$120548</b></div><div class="btn-blue">SOLD OUT</div></div>
</section>

<section class="team">
  <h2>OUR TEAM</h2>
  <div class="rule"></div>
  <div class="bubble" style="left:225px;top:120px;width:360px;height:155px">Nora has guided coastal buyers for two decades, known for calm advice, sharp pricing and a gift for finding the home each family truly wants.</div>
  <svg class="abs" style="left:325px;top:273px" width="30" height="24" viewBox="0 0 30 24"><path d="M0 0h30L8 22z" fill="#fff" stroke="#cfd4da" stroke-width="1.5"/><path d="M1 0h28" stroke="#fff" stroke-width="3"/></svg>
  <div class="bubble" style="left:575px;top:75px;width:375px;height:150px">Ellis leads our marketing and listings, bringing each home to life with care, clear detail and a strong network of buyers at home and abroad.</div>
  <svg class="abs" style="left:668px;top:223px" width="30" height="24" viewBox="0 0 30 24"><path d="M0 0h30L8 22z" fill="#fff" stroke="#cfd4da" stroke-width="1.5"/><path d="M1 0h28" stroke="#fff" stroke-width="3"/></svg>
  <div class="avatar" role="img" aria-label="Portrait of Nora Marlow" style="left:308px;top:318px"></div>
  <div class="member" style="left:410px;top:335px">NORA MARLOW<small>Founding Partner</small></div>
  <div class="avatar" role="img" aria-label="Portrait of Ellis" style="left:662px;top:292px;background:linear-gradient(160deg,#a8927c,#5a4a3e)"></div>
  <div class="member" style="left:764px;top:310px">ELLIS<small>Listing Director</small></div>
</section>

<section class="consult">
  <div class="photo" role="img" aria-label="Smiling advisor wearing a headset"></div>
  <svg class="consult-panel" width="1200" height="305" viewBox="0 0 1200 305"><path d="M0 0H620L520 305H0z" fill="#3a86d4"/><path d="M620 0h18L538 305h-18z" fill="#ffffff" opacity=".5"/></svg>
  <h2>REQUEST <b>A CONSULT</b></h2>
  <p>GET STARTED BY FILLING OUT OUR ONLINE ENQUIRY FORM, WE'LL GET IN TOUCH WITHIN <b>24 HOURS</b></p>
  <div class="mail-ring"><svg width="44" height="32" viewBox="0 0 44 32"><rect x="1" y="1" width="42" height="30" rx="3" fill="#888"/><path d="M2 3l20 15L42 3" fill="none" stroke="#d9dde2" stroke-width="3"/></svg></div>
  <div class="input" style="top:22px">Name</div>
  <div class="input" style="top:70px">Email</div>
  <div class="input" style="top:118px">Phone Number</div>
  <div class="input" style="top:166px;height:72px">Your Message</div>
  <div class="btn-blue">Send</div>
</section>

<section class="blog">
  <h2>LATEST FROM BLOG</h2>
  <div class="post" style="left:133px">
    <div class="photo" role="img" aria-label="Living room with sea view" style="background:linear-gradient(160deg,#8bb6dd,#4c5e72 60%,#b49878)"></div>
    <div class="date">FEB<b>28</b></div><div class="date-icon" style="top:72px"><svg width="14" height="12" viewBox="0 0 14 12"><rect x="1" y="3" width="12" height="8" fill="#fff"/><rect x="4" y="1" width="6" height="3" fill="#fff"/></svg></div><div class="date-icon" style="top:110px"><svg width="14" height="12" viewBox="0 0 14 12"><path d="M1 1h12v7H6l-3 3V8H1z" fill="#fff"/></svg></div>
    <h3>Benefits of a reputable cabinet...</h3><div class="meta">MAY 30, 2014 | 3 COMMENTS | ♥ 16</div>
    <p>Simple ways to plan a coastal home that stays bright and calm all year.</p>
    <div class="btn-blue">Read More</div>
  </div>
  <div class="post" style="left:443px">
    <div class="photo" role="img" aria-label="Infinity pool overlooking ocean" style="background:linear-gradient(160deg,#3d6ea8,#6f8a9e 50%,#2e4d6e)"></div>
    <div class="date">FEB<b>26</b></div><div class="date-icon" style="top:72px"><svg width="14" height="12" viewBox="0 0 14 12"><rect x="1" y="3" width="12" height="8" fill="#fff"/><rect x="4" y="1" width="6" height="3" fill="#fff"/></svg></div><div class="date-icon" style="top:110px"><svg width="14" height="12" viewBox="0 0 14 12"><path d="M1 1h12v7H6l-3 3V8H1z" fill="#fff"/></svg></div>
    <h3>Benefits of a reputable cabinet...</h3><div class="meta">MAY 30, 2014 | 3 COMMENTS | ♥ 16</div>
    <p>What buyers look for first when touring a home right on the sand.</p>
    <div class="btn-blue">Read More</div>
  </div>
  <div class="post" style="left:785px">
    <div class="photo" role="img" aria-label="Terrace at sunset over the sea" style="background:linear-gradient(160deg,#2b4f86,#c28a55 55%,#4a3a30)"></div>
    <div class="date">FEB<b>25</b></div><div class="date-icon" style="top:72px"><svg width="14" height="12" viewBox="0 0 14 12"><rect x="1" y="3" width="12" height="8" fill="#fff"/><rect x="4" y="1" width="6" height="3" fill="#fff"/></svg></div><div class="date-icon" style="top:110px"><svg width="14" height="12" viewBox="0 0 14 12"><path d="M1 1h12v7H6l-3 3V8H1z" fill="#fff"/></svg></div>
    <h3>Benefits of a reputable cabinet...</h3><div class="meta">MAY 30, 2014 | 3 COMMENTS | ♥ 16</div>
    <p>How to price a waterfront estate so it sells fast and at its best.</p>
    <div class="btn-blue">Read More</div>
  </div>
</section>

<footer class="site-footer">
  <h4 style="left:133px;top:38px">Quick Links</h4>
  <ul class="links" style="left:133px"><li>Home</li><li>About</li><li>Property Search</li><li>Explore O.C</li></ul>
  <ul class="links" style="left:290px"><li>Team</li><li>Videos</li><li>Blog</li><li>Contact</li></ul>
  <div class="follow">Follow Us On <span></span><span></span><span></span><span></span></div>
  <div class="video-tab">
    <h4 style="left:20px;top:48px">Our Video</h4>
    <div class="video" role="img" aria-label="Video still of a seaside home">
      <div class="play"><svg width="14" height="16" viewBox="0 0 14 16"><path d="M1 1l12 7-12 7z" fill="#fff"/></svg></div>
      <div class="video-bar"></div>
    </div>
  </div>
  <h4 style="left:810px;top:38px">Newsletter Signup</h4>
  <div class="news-box">Join our list for new listings, market notes and coastal news.
    <div class="news-input">✉ Email Address</div><div class="news-go">GO</div>
  </div>
  <div class="copyright">© 2015 Marlow on the Tide. All Rights Reserved.</div>
</footer>

</body>
</html>
```